Lucia Verena a furniture, interior design and home decor Brand

I need complete stationary for a new brand, business card, postcard, letter head, shipping envelopes, tissue paper, etc... I would like to use copper foil on some of these items. I have a logo design. I would like to see

Target Market(s)

Furniture,Interior Design & Home Decor

Industry/Entity Type

Interior Design

Colors
606060
7f7f7f

Requirements
Must have
• My signature style is spanish medeterrenean, my brand colors is charcoal gray with copper. Would love to see a wrought iron panel illustration created, I have attahced a few samples of wrought iron illustration I am attracted to, also an example of packing that has the pattern in foil.
Should not have
• Will not be using the word Design, only Lucia Verena and LV icon

```html
<!DOCTYPE html>
<html lang="en">
<head>
<meta charset="utf-8">
<title>Lucia Verena Letterhead</title>
<link href="https://fonts.googleapis.com/css2?family=Montserrat:ital,wght@0,400;0,500;0,700;1,700&display=swap" rel="stylesheet">
<style>
  :root {
    --backdrop: #9a9a9a;
    --paper: #eeeeef;
    --ink: #1c1c1c;
    --muted: #3c3c3c;
    --copper: #c4622d;
    --copper-light: #e08a55;
    --charcoal: #48474c;
  }
  * { margin: 0; padding: 0; box-sizing: border-box; }
  html, body { width: 1200px; height: 1200px; overflow: hidden; }
  body {
    background: var(--backdrop);
    font-family: "Montserrat", sans-serif;
    color: var(--ink);
    position: relative;
  }
  .letterhead {
    position: absolute;
    left: 197px; top: 30px;
    width: 806px; height: 1140px;
    background: var(--paper);
    overflow: hidden;
  }
  .brand {
    position: absolute;
    left: 76px; top: 53px;
    display: flex; align-items: center; gap: 18px;
  }
  .brand-circle {
    width: 104px; height: 104px;
    border: 1.5px solid var(--copper);
    border-radius: 50%;
  }
  .brand-name {
    font-weight: 400;
    font-size: 36px;
    color: var(--copper);
    letter-spacing: 0.5px;
  }
  .contact {
    position: absolute;
    right: 81px; top: 50px;
    text-align: right;
    font-size: 12px;
    line-height: 15px;
    color: var(--muted);
  }
  .contact .address { margin-bottom: 19px; }
  .contact-line {
    display: flex; justify-content: flex-end; align-items: center;
    gap: 7px; height: 20px;
  }
  .contact-line svg { width: 15px; height: 15px; }
  .date {
    position: absolute; left: 76px; top: 218px;
    font-size: 15px;
  }
  .recipient {
    position: absolute; left: 76px; top: 265px;
    font-size: 15px; line-height: 23px;
  }
  .recipient .name { font-weight: 700; }
  .salutation {
    position: absolute; left: 79px; top: 355px;
    font-size: 16px; font-weight: 700; font-style: italic;
  }
  .body-copy {
    position: absolute; left: 79px; top: 409px;
    width: 648px;
    font-size: 13.4px; line-height: 23.1px;
    text-align: justify;
  }
  .body-copy p + p { margin-top: 23.1px; }
  .signature-mark {
    position: absolute; left: 570px; top: 912px;
    width: 122px; height: 36px;
    background: linear-gradient(90deg, rgba(28,28,28,0.15), rgba(28,28,28,0.05));
    border-radius: 4px;
  }
  .sign-off {
    position: absolute; left: 571px; top: 953px;
    font-size: 15px; line-height: 16px;
  }
  .sign-off .role { font-size: 11.5px; font-weight: 500; }
  .corner-swoop {
    position: absolute; left: 0; bottom: 0;
    width: 300px; height: 220px;
  }
</style>
</head>
<body>
  <main class="letterhead">
    <header>
      <div class="brand">
        <div class="brand-circle"></div>
        <span class="brand-name">Lucia Verena</span>
      </div>
      <div class="contact">
        <div class="address">48 Alder Lane<br>Brookvale, AB, T2K 4M8</div>
        <div class="contact-line">403-555-0182
          <svg viewBox="0 0 16 16"><circle cx="8" cy="8" r="8" fill="var(--copper)"/><path d="M5.5 4.5c-1 1.5 0 4 2 5.8 1.6 1.4 3.3 1.8 4.3 1l-1.4-1.6-1.2.6-2.3-2.4.6-1.2z" fill="#fff"/></svg>
        </div>
        <div class="contact-line">hello@luciaverena.com
          <svg viewBox="0 0 16 16"><circle cx="8" cy="8" r="7.2" fill="none" stroke="var(--copper)" stroke-width="1.4"/><rect x="4.3" y="5.3" width="7.4" height="5.4" fill="none" stroke="var(--copper)" stroke-width="1.1"/><path d="M4.3 5.3 8 8.4l3.7-3.1" fill="none" stroke="var(--copper)" stroke-width="1.1"/></svg>
        </div>
        <div class="contact-line">www.luciaverena.com
          <svg viewBox="0 0 16 16"><circle cx="8" cy="8" r="7.2" fill="none" stroke="var(--copper)" stroke-width="1.4"/><circle cx="8" cy="8" r="4" fill="none" stroke="var(--copper)" stroke-width="1"/><path d="M4 8h8M8 4v8M5 5.8h6M5 10.2h6" stroke="var(--copper)" stroke-width="0.8"/></svg>
        </div>
      </div>
    </header>

    <p class="date">January 14, 2016</p>
    <div class="recipient">
      <p class="name">Mr. Paul Hartley</p>
      <p>Photographer</p>
    </div>
    <p class="salutation">Dear Mr. Paul Hartley</p>

    <section class="body-copy">
      <p>Lorem ipsum dolor sit amet, consectetur adipiscing elit. Ut feugiat erat interdum augue interdum, vitae fringilla ante vehicula. Pellentesque ultrices nulla id accumsan scelerisque. Suspendisse vitae luctus dui. Cras sed dictum lorem. Donec non gravida lacus. Phasellus et quam et mi commodo malesuada ac bibendum lorem. Fusce eleifend, metus vel convallis fringilla, ipsum dui egestas arcu, at hendrerit elit nisl eget metus. Proin eget fringilla eros. Nunc eros metus, molestie in ligula non, imperdiet lobortis massa. Proin accumsan posuere erat, vitae adipiscing sem commodo eu.</p>
      <p>Morbi a faucibus nulla. Nulla id leo ac massa fermentum molestie. Integer at gravida risus. Sed auctor odio augue. Mauris eu leo a orci placerat bibendum sed ac nulla. Sed risus mauris, vestibulum sit amet egestas at, pulvinar sed mauris. In velit purus, laoreet ac lectus vitae, ornare posuere tortor. Phasellus mattis accumsan vestibulum.</p>
      <p>Donec cursus libero id convallis egestas. Aliquam quam quam, facilisis eget diam at, ultricies sagittis justo. Integer massa nibh, gravida eu nulla sagittis, feugiat ultrices magna. Ut commodo venenatis tortor, sed dignissim mauris congue non.</p>
    </section>

    <div class="signature-mark" role="img" aria-label="Handwritten signature"></div>
    <div class="sign-off">
      <p>Elena Marsh,</p>
      <p class="role">Photographer</p>
    </div>

    <svg class="corner-swoop" viewBox="0 0 300 220" aria-hidden="true">
      <defs>
        <linearGradient id="copperEdge" x1="0" y1="0" x2="1" y2="1">
          <stop offset="0" stop-color="var(--copper-light)"/>
          <stop offset="1" stop-color="var(--copper)"/>
        </linearGradient>
      </defs>
      <path d="M0 220 L0 142 C40 140 120 70 160 28 C165 120 172 190 253 220 Z" fill="var(--charcoal)"/>
      <path d="M160 28 C165 120 172 190 253 220" fill="none" stroke="url(#copperEdge)" stroke-width="3"/>
    </svg>
  </main>
</body>
</html>
```